Clean business card with logo provided

I want a card that will stand out among the masses. I need the color and image to show professionalism and yet have a family appeal showing that I only deal with win/win scenarios. The back of the card will be used to take notes about the individual so I can use that in my database entry. I like modern design but need professionalism in it also. It needs to fit my "clean, safe, and affordable housing" motto. I need to be able to write on the file and update the card details for my employees.

Target Market(s)

Investors looking to make investment income through real estate

Industry/Entity Type

Real Estate

Contact Information for Business Card

Troy Vandemark
blank address, city, st, zip code
480-555-0147
troyvandemark@quillrentals.example
www.quillrentals.example

Font styles to use
Sans Serif

Requirements
Must have
• I would like the back of the card to have lines for info. example
• Met/Visited: Date:
• Interets:
Nice to have
• I want the cards color to match the logo background color. Font with details to be san serif and black. I want the card rectangular with square corners. Standard business card size. I would like to see cards designed with both images to see which i prefer more.

```html
<!DOCTYPE html>
<html lang="en">
<head>
<meta charset="utf-8">
<title>Quill Rentals LLC – Business Card</title>
<link rel="stylesheet" href="https://fonts.googleapis.com/css2?family=Open+Sans:wght@400;600;700&display=swap">
<style>
  :root {
    --stage: #2e2f33;
    --card: #ffffff;
    --teal: #00b5cc;
    --ink: #111111;
    --rule: #1a1a1a;
  }
  * { box-sizing: border-box; margin: 0; padding: 0; }
  html, body { width: 1200px; height: 864px; overflow: hidden; }
  body {
    background: var(--stage);
    font-family: "Open Sans", Arial, sans-serif;
    position: relative;
  }
  .card {
    position: absolute;
    left: 330px;
    width: 540px;
    height: 309px;
    background: var(--card);
    overflow: hidden;
  }
  .card--back { top: 100px; }
  .card--front { top: 455px; }

  /* Back: note-taking side */
  .back-art {
    position: absolute;
    left: 0; top: 0;
    width: 150px; height: 100%;
    background: linear-gradient(160deg, var(--teal) 0%, #14c2d6 60%, #e8f8fb 100%);
  }
  .note-field { position: absolute; }
  .note-field__label {
    display: block;
    color: var(--teal);
    font-weight: 700;
    font-size: 13px;
    letter-spacing: 0.3px;
    text-align: center;
    margin-bottom: 12px;
  }
  .note-field__line { display: block; height: 1px; background: var(--rule); }
  .note-field--date { top: 66px; left: 215px; width: 250px; }
  .note-field--interests { top: 130px; left: 200px; width: 250px; }
  .note-field--problems { top: 194px; left: 185px; width: 250px; }

  /* Front: contact side */
  .brand { position: absolute; left: 100px; top: 48px; }
  .brand__name {
    color: var(--teal);
    font-weight: 600;
    font-size: 30px;
    letter-spacing: 1px;
    line-height: 1;
  }
  .brand__tagline {
    color: var(--teal);
    font-weight: 600;
    font-size: 8.5px;
    margin-top: 6px;
  }
  .name-row {
    position: absolute;
    left: 58px; right: 0; top: 164px;
    display: flex;
    align-items: flex-end;
    gap: 8px;
  }
  .name-row__rule {
    flex: 1;
    height: 1.5px;
    background: var(--rule);
    margin-bottom: 4px;
  }
  .name-row__tail {
    width: 18px;
    height: 1.5px;
    background: var(--rule);
    margin-bottom: 4px;
  }
  .person-name {
    color: var(--teal);
    font-weight: 600;
    font-size: 19px;
    line-height: 1.1;
    white-space: nowrap;
  }
  .contact-list {
    position: absolute;
    right: 14px; top: 206px;
    list-style: none;
    text-align: right;
    color: var(--ink);
    font-size: 13px;
    line-height: 22px;
  }
  .contact-list li { display: flex; justify-content: flex-end; align-items: center; gap: 8px; white-space: nowrap; }
  .contact-list svg { width: 11px; height: 11px; fill: var(--teal); flex: none; }
</style>
</head>
<body>

<section class="card card--back" aria-label="Card back with note lines">
  <div class="back-art" role="img" aria-label="Large teal manta ray illustration sweeping across the left edge"></div>
  <div class="note-field note-field--date">
    <span class="note-field__label">VISITED DATE:</span>
    <span class="note-field__line"></span>
  </div>
  <div class="note-field note-field--interests">
    <span class="note-field__label">INTERETS:</span>
    <span class="note-field__line"></span>
  </div>
  <div class="note-field note-field--problems">
    <span class="note-field__label">PROBLEMS:</span>
    <span class="note-field__line"></span>
  </div>
</section>

<section class="card card--front" aria-label="Card front with contact details">
  <div class="brand">
    <div class="brand__name">Quill Rentals LLC</div>
    <div class="brand__tagline">Providing clean, safe, and affordable housing</div>
  </div>
  <div class="name-row">
    <span class="name-row__rule"></span>
    <span class="person-name">Troy Vandemark</span>
    <span class="name-row__tail"></span>
  </div>
  <ul class="contact-list">
    <li>480-555-0147
      <svg viewBox="0 0 24 24" aria-hidden="true"><path d="M6.6 10.8a15.1 15.1 0 0 0 6.6 6.6l2.2-2.2a1 1 0 0 1 1-.25 11.4 11.4 0 0 0 3.6.57 1 1 0 0 1 1 1V20a1 1 0 0 1-1 1A17 17 0 0 1 3 4a1 1 0 0 1 1-1h3.5a1 1 0 0 1 1 1c0 1.25.2 2.45.57 3.57a1 1 0 0 1-.25 1z"/></svg>
    </li>
    <li>troyvandemark@quillrentals.example
      <svg viewBox="0 0 24 24" aria-hidden="true"><path d="M2 5h20v14H2z M3.5 6.5 12 13l8.5-6.5"/></svg>
    </li>
    <li>www.quillrentals.example
      <svg viewBox="0 0 24 24" aria-hidden="true"><circle cx="12" cy="12" r="10"/></svg>
    </li>
    <li>12345, Address Goes Here Country Name, 123456</li>
  </ul>
</section>

</body>
</html>
```